Email template for construction companies

Hello, I'm looking to build out an html email template for our email marketing. I'd like it to compliment our website, but not be an exact replication of it.

This template will be used in all of our email marketing campaigns. We provide financial support for construction companies, so it needs to express stability and confidence, but not the stuffiness of a traditional bank.

Target Market(s)

Construction companies (subcontractors specifically)

Industry/Entity Type

Construction Company

Font styles to use
Serif

Requirements
Must have
• Must compliment our website, but not be a replica.
Should not have
• Should not be an exact replica of our website.

```html
<!DOCTYPE html>
<html lang="en">
<head>
<meta charset="utf-8">
<title>Funding the Construction Industrey!</title>
<link rel="stylesheet" href="https://fonts.googleapis.com/css2?family=Roboto+Slab:wght@100;200;300;700&family=Roboto:wght@300;400;500;700&display=swap">
<style>
  :root {
    --brand-blue: #4a87c9;
    --heading-blue: #3f84c8;
    --halo-blue: #a8c6e6;
    --frame-blue: #d7e5f4;
    --rule-blue: #a9c7e8;
    --ink-dark: #1f2a36;
    --body-text: #3a3d42;
    --footer-dark: #2b2e33;
    --footer-darker: #222529;
    --footer-muted: #4b4f55;
    --icon-grey: #8a8e94;
    --white: #ffffff;
  }
  * { box-sizing: border-box; margin: 0; padding: 0; }
  html, body { width: 944px; height: 1200px; overflow: hidden; background: var(--white); }
  body { font-family: "Roboto", Arial, sans-serif; color: var(--body-text); }
  .sheet { position: relative; width: 944px; height: 1200px; overflow: hidden; background: var(--white); }

  .hero { position: absolute; left: 0; top: 0; width: 944px; height: 318px; background: var(--brand-blue); overflow: hidden; }
  .hero-art { position: absolute; left: 0; top: 0; width: 944px; height: 318px; }
  .hero-title { position: absolute; left: 57px; top: 96px; font-family: "Roboto Slab", "Zilla Slab", "Rockwell", "DejaVu Serif", serif; font-size: 50px; line-height: 62px; letter-spacing: 0.2px; font-weight: 400; }
  .hero-title .line { display: block; white-space: nowrap; }
  .hero-title .strong-white { color: var(--white); font-weight: 700; }
  .hero-title .thin-white { color: var(--white); font-weight: 200; }
  .hero-title .strong-dark { color: var(--ink-dark); font-weight: 700; }
  .hero-title .thin-dark { color: var(--ink-dark); font-weight: 100; }

  .section-heading { position: absolute; font-family: "Roboto", Arial, sans-serif; font-weight: 500; font-size: 28px; color: var(--heading-blue); white-space: nowrap; }
  .section-copy { position: absolute; font-size: 15px; line-height: 18.8px; color: var(--body-text); font-weight: 400; }
  .section-copy p + p { margin-top: 8px; }

  .photo-frame { position: absolute; background: var(--frame-blue); padding: 12px; }
  .photo-frame .photo { width: 100%; height: 100%; }

  .change-heading { left: 57px; top: 360px; }
  .change-copy { left: 57px; top: 406px; width: 500px; }
  .change-photo { left: 596px; top: 365px; width: 279px; height: 215px; }
  .change-photo .photo { background: linear-gradient(135deg, #8a6a46 0%, #c8b79c 45%, #7d8a6a 100%); }

  .divider { position: absolute; left: 57px; top: 635px; width: 824px; height: 2px; background: var(--rule-blue); }

  .mission-photo { left: 57px; top: 678px; width: 293px; height: 226px; }
  .mission-photo .photo { background: linear-gradient(135deg, #c9a36c 0%, #e2c89d 40%, #3a4f86 100%); }
  .mission-heading { left: 376px; top: 676px; }
  .mission-copy { left: 376px; top: 722px; width: 506px; }

  .footer { position: absolute; left: 0; top: 962px; width: 944px; height: 238px; background: var(--footer-dark); }
  .footer-base { position: absolute; left: 0; top: 133px; width: 944px; height: 105px; }
  .contact-list { position: absolute; left: 57px; top: 26px; list-style: none; }
  .contact-item { display: flex; align-items: center; height: 34px; color: var(--white); font-size: 19px; font-weight: 400; }
  .contact-item.phone { font-weight: 700; }
  .contact-item svg { width: 22px; height: 22px; margin-right: 14px; flex: none; }

  .brand { position: absolute; left: 488px; top: 50px; display: flex; align-items: center; }
  .brand-dot { width: 72px; height: 72px; border-radius: 50%; background: var(--white); margin-right: 14px; }
  .brand-name { font-family: "Roboto", Arial, sans-serif; font-weight: 300; font-size: 44px; color: var(--white); letter-spacing: 0.3px; }

  .follow { position: absolute; left: 57px; top: 155px; display: flex; align-items: center; color: var(--white); font-size: 19px; }
  .follow-label { margin-right: 18px; }
  .social-square { width: 16px; height: 16px; background: var(--footer-muted); margin-right: 9px; }
  .copyright { position: absolute; left: 57px; top: 198px; font-size: 11px; color: #44484e; }
</style>
</head>
<body>
<div class="sheet">

  <header class="hero">
    <svg class="hero-art" viewBox="0 0 944 318" aria-hidden="true">
      <circle cx="662" cy="245" r="144" fill="var(--halo-blue)"/>
    </svg>
    <svg class="hero-art" viewBox="0 0 944 318" role="img" aria-label="Illustration of a small house in front of a stack of dollar banknotes">
      <rect x="728" y="112" width="152" height="206" fill="#2fa6c4" opacity="0.7"/>
      <rect x="560" y="150" width="170" height="168" fill="#f5b13a" opacity="0.8"/>
    </svg>
    <h1 class="hero-title">
      <span class="line strong-white">Funding</span>
      <span class="line"><span class="thin-white">the </span><span class="strong-dark">Construction</span></span>
      <span class="line thin-dark">Industrey!</span>
    </h1>
  </header>

  <h2 class="section-heading change-heading">A Desire For Change</h2>
  <div class="section-copy change-copy">
    <p>Financial stress and limited business capabilities are destroying construction professionals. By supporting the financial needs of these companies, we’re building better, stronger businesses. When business is strong and stable, construction companies can do amazing things. They are the ones who will literally build our future and build better communities for us to be a part of. We’re not only building better lives for contractors and their families, but also impacting the population at large through positive economic, functional,improvements that our support helps create.</p>
  </div>
  <div class="photo-frame change-photo">
    <div class="photo" role="img" aria-label="Photo of a construction worker in a hard hat and safety vest using a power drill on a timber frame"></div>
  </div>

  <div class="divider"></div>

  <div class="photo-frame mission-photo">
    <div class="photo" role="img" aria-label="Photo of a smiling builder in a blue hard hat standing in front of stacked lumber"></div>
  </div>
  <h2 class="section-heading mission-heading">Mission &amp; Values</h2>
  <div class="section-copy mission-copy">
    <p>Our mission is to strengthen the construction industry by providing the resources needed to propel business growth and support an industry that has long been underserved and neglected.</p>
    <p>They are the ones who will literally build our future and build better communities for us to be a part of. We’re not only building better lives for contractors and their families, but also impacting the population at large through positive economic, functional,improvements that our support helps create.</p>
  </div>

  <footer class="footer">
    <svg class="footer-base" viewBox="0 0 944 105" preserveAspectRatio="none" aria-hidden="true">
      <polygon points="0,0 375,0 430,38 944,38 944,105 0,105" fill="var(--footer-darker)"/>
    </svg>

    <ul class="contact-list">
      <li class="contact-item phone">
        <svg viewBox="0 0 22 22" aria-hidden="true"><circle cx="11" cy="11" r="10" fill="none" stroke="var(--icon-grey)" stroke-width="1.5"/><path d="M7.5 6.5l2 0.2 0.8 2.3-1.2 1a6 6 0 0 0 3 3l1-1.2 2.3 0.8 0.2 2c-4.5 0.8-8.9-3.6-8.1-8.1z" fill="var(--icon-grey)"/></svg>
        +1 (800) 555-0147
      </li>
      <li class="contact-item">
        <svg viewBox="0 0 22 22" aria-hidden="true"><circle cx="11" cy="11" r="10" fill="none" stroke="var(--icon-grey)" stroke-width="1.5"/><rect x="6" y="8" width="10" height="7" fill="none" stroke="var(--icon-grey)" stroke-width="1.3"/><path d="M6 8l5 4 5-4" fill="none" stroke="var(--icon-grey)" stroke-width="1.3"/></svg>
        info@buildledger.com
      </li>
      <li class="contact-item">
        <svg viewBox="0 0 22 22" aria-hidden="true"><circle cx="11" cy="11" r="10" fill="none" stroke="var(--icon-grey)" stroke-width="1.5"/><circle cx="11" cy="11" r="5.5" fill="none" stroke="var(--icon-grey)" stroke-width="1.2"/><path d="M5.5 11h11M11 5.5v11" stroke="var(--icon-grey)" stroke-width="1.2"/></svg>
        www.buildledger.com
      </li>
    </ul>

    <div class="brand">
      <div class="brand-dot"></div>
      <span class="brand-name">BuildLedger</span>
    </div>

    <div class="follow">
      <span class="follow-label">Follow:</span>
      <span class="social-square"></span>
      <span class="social-square"></span>
      <span class="social-square"></span>
      <span class="social-square"></span>
      <span class="social-square"></span>
    </div>
    <p class="copyright">Copyright © 2016 BuildLedger. All Rights Reserved.</p>
  </footer>

</div>
</body>
</html>
```